Young and modern Electrical company working in the commercial arena.

Wanting a business card design thats modern and will last. Maybe Minimalist? Happy to look at changing my logo

Target Market(s)

Builders, Project Managers

Industry/Entity Type

Electrical

Contact Information for Business Card

Name
Address
Phone number
Job title

Logo Text

our name or just the logo i'm open to ideas

Font styles to use
Sans Serif

Requirements
Nice to have
• would like to keep the purple in our current logo. it's kinda unique to our market
Should not have
• Don't want it to be to busy. simple is best i think

```html
<!DOCTYPE html>
<html lang="en">
<head>
<meta charset="utf-8">
<title>Voltline Electrical – Business Card</title>
<link rel="stylesheet" href="https://fonts.googleapis.com/css2?family=Lato:wght@400;700&display=swap">
<style>
  :root {
    --purple: #6f4ea3;
    --black: #1b1b1b;
    --white: #ffffff;
    --ink: #2a2a2a;
    --stage: #2b2b2d;
  }
  * { margin: 0; padding: 0; box-sizing: border-box; }
  html, body { width: 1200px; height: 852px; overflow: hidden; background: var(--stage); font-family: "Lato", sans-serif; }
  .canvas { position: relative; width: 1200px; height: 852px; }
  .card {
    position: absolute; left: 290px; width: 620px; height: 354px;
    border-radius: 18px; overflow: hidden;
    box-shadow: 0 10px 30px rgba(0,0,0,.45);
  }
  .card--back { top: 46px; background: var(--purple); color: var(--white); }
  .card--front { top: 450px; background: var(--white); color: var(--ink); }

  .back-logo {
    position: absolute; left: 0; right: 0; top: 140px; text-align: center;
    font-size: 50px; font-weight: 700; letter-spacing: 1px; color: var(--white);
  }
  .back-web { position: absolute; right: 48px; bottom: 34px; font-size: 14px; letter-spacing: .3px; }

  .front-logo {
    position: absolute; left: 40px; top: 112px;
    font-size: 30px; font-weight: 700; color: var(--purple); letter-spacing: .5px;
    display: flex; align-items: center; gap: 10px;
  }
  .front-logo .dot { width: 12px; height: 12px; border-radius: 50%; background: var(--purple); }
  .person { position: absolute; right: 40px; top: 52px; text-align: right; }
  .person__name { font-size: 28px; font-weight: 700; color: var(--purple); letter-spacing: 1px; }
  .person__title { font-size: 14px; color: var(--ink); margin-top: 2px; }
  .divider { position: absolute; left: 40px; right: 40px; top: 160px; height: 1px; background: var(--ink); }

  .contacts { position: absolute; left: 40px; top: 176px; list-style: none; font-size: 15px; line-height: 21px; }
  .contacts li { display: flex; align-items: center; gap: 10px; }
  .contacts svg { width: 12px; height: 12px; fill: var(--purple); flex: none; }
  .contacts .accent { color: var(--purple); }

  .wave { position: absolute; left: 0; top: 0; width: 620px; height: 354px; }
  .address {
    position: absolute; right: 36px; bottom: 48px; text-align: right;
    color: var(--white); font-size: 15px; line-height: 20px;
  }
</style>
</head>
<body>
<main class="canvas">
  <section class="card card--back">
    <div class="back-logo">voltline electrical</div>
    <div class="back-web">www.voltlineelectrical.com.au</div>
  </section>

  <section class="card card--front">
    <svg class="wave" viewBox="0 0 620 354" aria-hidden="true">
      <path d="M0,282 C170,322 300,296 380,246 C460,196 525,176 620,164 L620,354 L0,354 Z" fill="var(--black)"/>
      <path d="M0,322 C190,348 320,318 405,268 C485,220 545,202 620,192 L620,354 L0,354 Z" fill="var(--purple)" stroke="var(--white)" stroke-width="5"/>
    </svg>

    <div class="person">
      <div class="person__name">DANIEL HARPER</div>
      <div class="person__title">Director</div>
    </div>
    <div class="front-logo"><span class="dot"></span>voltline electrical</div>
    <div class="divider"></div>

    <ul class="contacts">
      <li><svg viewBox="0 0 24 24"><path d="M6.6 10.8a15 15 0 0 0 6.6 6.6l2.2-2.2a1 1 0 0 1 1-.25 11.4 11.4 0 0 0 3.6.57 1 1 0 0 1 1 1V20a1 1 0 0 1-1 1A17 17 0 0 1 3 4a1 1 0 0 1 1-1h3.5a1 1 0 0 1 1 1c0 1.25.2 2.45.57 3.57a1 1 0 0 1-.25 1z"/></svg>0400 123 456</li>
      <li><svg viewBox="0 0 24 24"><path d="M7 1h10a2 2 0 0 1 2 2v18a2 2 0 0 1-2 2H7a2 2 0 0 1-2-2V3a2 2 0 0 1 2-2zm0 3v14h10V4zm5 15.5a1.2 1.2 0 1 0 0 2.4 1.2 1.2 0 0 0 0-2.4z"/></svg>0411 987 654</li>
      <li><svg viewBox="0 0 24 24"><path d="M2 5h20v14H2zm2 2v.5l8 5 8-5V7zm0 2.9V17h16V9.9l-8 5z"/></svg>admin@voltlineelectrical.com.au</li>
      <li><svg viewBox="0 0 24 24"><circle cx="12" cy="12" r="10"/></svg>www.<span class="accent">voltlineelectrical</span>.com.au</li>
    </ul>

    <div class="address">Harbour Lane,<br>Marrickville NSW, Australia</div>
  </section>
</main>
</body>
</html>
```